Food Company needs packaging label for trade shows

We need a packaging label designed for a trade show we are attending in July 2023. The packaging will have a font and back section that will be printed on stickers and be placed on the packaging.
Two concept retail products have been developed and packaged into small foil packages that will be given out at trade shows as samples.
2 designs are needed for this project and will need to have similar design flow to match but showcase different product attributes.
Bright colors and pinks are preferred to stand out.
The Final design label should showcase the company logo, product name, picture, attributes on the front. The back will have our company information, basic nutritional information, ingredient listing.
Product 1: packaging label needs to be printed on 4" wide x 4" high
Product 2: packaging label needs to be printed on 5" wide x 2.5" high

Target Market(s)

Food ingredient trade show

Industry/Entity Type

Food

Colors

Designer to choose colors to be used in the design.

Requirements
Must have
• Company logo, product name and information, product picture
Nice to have
• Bright colors that will stand out when the sample is given

```html
<!DOCTYPE html>
<html lang="en">
<head>
<meta charset="utf-8">
<title>Brightfield Sample Labels</title>
<link href="https://fonts.googleapis.com/css2?family=Bubblegum+Sans&family=Open+Sans:wght@700;800&display=swap" rel="stylesheet">
<style>
  :root {
    --page: #ebebed;
    --white: #ffffff;
    --cream: #f5f0e1;
    --pink: #ee6aa7;
    --purple: #5b2d8e;
    --yellow: #fcc84a;
    --orange: #f29a2e;
    --red: #e8383a;
    --brown: #5a3a17;
    --leaf: #5ab030;
  }
  * { margin: 0; padding: 0; box-sizing: border-box; }
  html, body { width: 1200px; height: 1186px; overflow: hidden; background: var(--page); }
  .canvas { position: relative; width: 1200px; height: 1186px; }
  .label { position: absolute; overflow: hidden; }
  .label--fiber { left: 318px; top: 104px; width: 565px; height: 564px; }
  .label--protein { left: 247px; top: 709px; width: 706px; height: 352px; }
  .label__shapes { position: absolute; inset: 0; }
  .abs { position: absolute; }
  .brand { position: absolute; display: flex; flex-direction: column; align-items: center; transform: translateX(-50%); }
  .brand__dot { width: 30px; height: 30px; border-radius: 50%; background: var(--leaf); margin-bottom: 6px; }
  .brand__name { font-family: "Open Sans", sans-serif; font-weight: 800; font-size: 10px; letter-spacing: 0.5px; color: var(--leaf); }
  .title, .subtitle, .weight, .stat {
    font-family: "Bubblegum Sans", cursive;
    position: absolute; text-align: center; white-space: nowrap; transform: translateX(-50%);
  }
  .title { letter-spacing: 3px; }
  .subtitle { color: var(--brown); letter-spacing: 1.5px; }
  .weight { color: var(--white); }
  .flavor {
    position: absolute; left: 0; background: var(--cream);
    font-family: "Open Sans", sans-serif; font-weight: 700;
    display: flex; align-items: center; white-space: nowrap;
  }
  .stat { color: var(--brown); line-height: 0.9; }
  .stat small { display: block; font-size: 0.45em; letter-spacing: 0.5px; }
  .claim {
    position: absolute; font-family: "Open Sans", sans-serif; font-weight: 800;
    text-align: center; line-height: 1; white-space: nowrap;
  }
  .claim--sm { width: 44px; font-size: 6px; color: var(--pink); }
  .claim--xs { width: 38px; font-size: 5px; color: var(--yellow); }
</style>
</head>
<body>
<main class="canvas">

  <!-- Product 1: 4 x 4 label -->
  <section class="label label--fiber">
    <svg class="label__shapes" width="565" height="564" viewBox="0 0 565 564">
      <rect width="565" height="564" fill="var(--pink)"/>
      <path d="M70,0 L460,0 C470,40 500,90 565,118 L565,288 C505,276 450,302 380,292 C300,280 250,302 170,294 C100,286 50,280 0,290 L0,130 C40,110 55,60 70,0 Z" fill="var(--white)"/>
      <path d="M0,85 C30,60 55,30 75,0" fill="none" stroke="var(--white)" stroke-width="6"/>
      <path d="M485,0 C500,30 525,40 565,40" fill="none" stroke="var(--white)" stroke-width="6"/>
      <rect x="6" y="352" width="355" height="50" fill="var(--purple)"/>
      <rect x="0" y="340" width="355" height="50" fill="var(--cream)"/>
      <circle cx="432" cy="360" r="58" fill="var(--white)" stroke="var(--purple)" stroke-width="9"/>
      <circle cx="485" cy="458" r="60" fill="var(--cream)" stroke="var(--purple)" stroke-width="9"/>
      <g fill="none" stroke="var(--white)" stroke-width="3">
        <circle cx="53" cy="462" r="33"/><circle cx="129" cy="462" r="33"/>
        <circle cx="205" cy="462" r="33"/><circle cx="281" cy="462" r="33"/>
        <circle cx="357" cy="462" r="33"/>
      </g>
      <g fill="var(--white)">
        <circle cx="53" cy="462" r="28"/><circle cx="129" cy="462" r="28"/>
        <circle cx="205" cy="462" r="28"/><circle cx="281" cy="462" r="28"/>
      </g>
      <g stroke="var(--pink)" stroke-width="3" fill="none">
        <line x1="40" y1="468" x2="66" y2="442"/>
        <rect x="123" y="442" width="12" height="22" rx="3"/><line x1="116" y1="468" x2="142" y2="442"/>
        <line x1="205" y1="440" x2="205" y2="470"/><line x1="192" y1="468" x2="218" y2="442"/>
        <path d="M281,470 L281,452 M281,456 C270,452 268,444 272,438 C280,440 282,448 281,456 C292,452 294,444 290,438"/>
      </g>
    </svg>

    <div class="brand" style="left:282px; top:26px;">
      <span class="brand__dot"></span>
      <span class="brand__name">BRIGHTFIELD</span>
    </div>
    <h1 class="title" style="left:286px; top:120px; font-size:74px; color:var(--purple);">FIBER TITANS</h1>
    <p class="subtitle" style="left:282px; top:208px; font-size:36px;">BAKED PEA SNACK</p>
    <p class="flavor" style="top:340px; width:355px; height:50px; padding-left:26px; font-size:20px; color:var(--purple);">LIGHTLY SALTED FLAVORED</p>
    <p class="stat" style="left:430px; top:330px; font-size:44px;">10%<small>PROTEIN</small></p>
    <p class="stat" style="left:485px; top:423px; font-size:48px;">10%<small>FIBER</small></p>

    <span class="claim claim--sm" style="left:31px; top:477px;">CORN &amp; RICE<br>FREE</span>
    <span class="claim claim--sm" style="left:107px; top:477px;">DAIRY<br>FREE</span>
    <span class="claim claim--sm" style="left:183px; top:477px;">GLUTEN<br>FREE</span>
    <span class="claim claim--sm" style="left:259px; top:477px;">PLANT<br>BASED</span>
    <span class="claim" style="left:327px; top:450px; width:60px; font-size:12px; color:var(--white);">NON<br>GMO</span>

    <p class="weight" style="left:282px; top:512px; font-size:30px;">20g</p>
  </section>

  <!-- Product 2: 5 x 2.5 label -->
  <section class="label label--protein">
    <svg class="label__shapes" width="706" height="352" viewBox="0 0 706 352">
      <rect width="706" height="352" fill="var(--yellow)"/>
      <path d="M105,0 L510,0 C530,30 560,55 600,62 C640,70 690,80 706,90 L706,200 C640,180 560,192 470,182 C380,172 300,192 200,182 C120,175 60,172 0,186 L0,95 C40,80 80,45 105,0 Z" fill="var(--white)"/>
      <path d="M0,40 C40,35 80,20 105,0" fill="none" stroke="var(--white)" stroke-width="6"/>
      <path d="M615,0 C625,30 660,40 706,38" fill="none" stroke="var(--white)" stroke-width="6"/>
      <rect x="6" y="212" width="445" height="60" fill="var(--orange)"/>
      <rect x="0" y="200" width="445" height="60" fill="var(--cream)"/>
      <circle cx="525" cy="222" r="50" fill="var(--white)" stroke="var(--orange)" stroke-width="8"/>
      <circle cx="627" cy="267" r="56" fill="var(--cream)" stroke="var(--orange)" stroke-width="8"/>
      <g fill="none" stroke="var(--white)" stroke-width="3">
        <circle cx="68" cy="311" r="27"/><circle cx="130" cy="311" r="27"/>
        <circle cx="191" cy="311" r="27"/><circle cx="253" cy="311" r="27"/>
        <circle cx="315" cy="311" r="27"/>
      </g>
      <g fill="var(--white)">
        <circle cx="68" cy="311" r="23"/><circle cx="130" cy="311" r="23"/>
        <circle cx="191" cy="311" r="23"/><circle cx="253" cy="311" r="23"/>
      </g>
      <g stroke="var(--yellow)" stroke-width="2.5" fill="none">
        <line x1="58" y1="315" x2="78" y2="295"/>
        <rect x="125" y="295" width="10" height="18" rx="3"/><line x1="120" y1="315" x2="140" y2="295"/>
        <line x1="191" y1="293" x2="191" y2="317"/><line x1="181" y1="315" x2="201" y2="295"/>
        <path d="M253,317 L253,303 M253,306 C244,303 243,297 246,292 C252,294 254,300 253,306 C262,303 263,297 260,292"/>
      </g>
    </svg>

    <div class="brand" style="left:353px; top:14px;">
      <span class="brand__dot" style="width:24px; height:24px; margin-bottom:5px;"></span>
      <span class="brand__name" style="font-size:9px;">BRIGHTFIELD</span>
    </div>
    <h1 class="title" style="left:353px; top:76px; font-size:54px; color:var(--red);">PROTEIN CRISPS</h1>
    <p class="subtitle" style="left:353px; top:134px; font-size:28px;">CRUNCHY PEA BAKED SNACK</p>
    <p class="flavor" style="top:200px; width:445px; height:60px; padding-left:15px; font-size:27px; color:var(--red);">MEDITERRANEAN FLAVORED</p>
    <p class="stat" style="left:525px; top:198px; font-size:40px;">50%<small>PROTEIN</small></p>
    <p class="stat" style="left:627px; top:236px; font-size:48px;">15%<small>FIBER</small></p>

    <span class="claim claim--xs" style="left:49px; top:321px;">CORN &amp; RICE<br>FREE</span>
    <span class="claim claim--xs" style="left:111px; top:321px;">DAIRY<br>FREE</span>
    <span class="claim claim--xs" style="left:172px; top:321px;">GLUTEN<br>FREE</span>
    <span class="claim claim--xs" style="left:234px; top:321px;">PLANT<br>BASED</span>
    <span class="claim" style="left:290px; top:302px; width:50px; font-size:10px; color:var(--white);">NON<br>GMO</span>

    <p class="weight" style="left:458px; top:298px; font-size:28px;">20g</p>
  </section>

</main>
</body>
</html>
```